Talvex Engineering Business card Design

We need to make business cards for our NDT and inspection company. The company is called Talvex Engineering. We want a professional modern feel business card. We have just completed the remaking of our website and would like to have business cards with the same feel and colours. The final design should communicate professionalism and cutting edge tech.

Target Market(s)

We sell to B2B Business clients. Our customer is an engineer or decision maker in the mechanical engineering / Oil and gas field.

Contact Information for Business Card

Please see the current business cards that we have uploaded to get the details. You can also look at our Website www.talvex-eng.example for more.

Requirements
Must have
• Less is more
Nice to have
• Less is more

```html
<!DOCTYPE html>
<html lang="en">
<head>
<meta charset="utf-8">
<title>Talvex Engineering – Business Card</title>
<link href="https://fonts.googleapis.com/css2?family=Arimo:wght@400;700&display=swap" rel="stylesheet">
<style>
  :root {
    --backdrop: #2b2b2d;
    --card: #1f2022;
    --card-edge: #26272a;
    --pattern: #2a2b2e;
    --ink: #f2f2f2;
    --ink-soft: #c9c9cb;
    --brand-grey: #bdbdbf;
    --accent-red: #b3121a;
    --accent-blue: #263a7a;
    --rule: #6a6a6e;
  }
  * { box-sizing: border-box; margin: 0; padding: 0; }
  html, body {
    width: 1200px; height: 1108px; overflow: hidden;
    background: var(--backdrop);
    font-family: "Arimo", Arial, sans-serif;
  }
  .stage {
    position: relative; width: 1200px; height: 1108px;
    display: flex; justify-content: center; align-items: center; gap: 80px;
  }
  .card {
    position: relative; width: 440px; height: 720px;
    background: var(--card); border-radius: 22px;
    box-shadow: 0 18px 40px rgba(0,0,0,.45);
    color: var(--ink); text-align: center; overflow: hidden;
  }

  /* Front */
  .card-front { padding-top: 120px; }
  .brand-mark {
    width: 120px; height: 96px; margin: 0 auto 22px;
    border-radius: 50%; background: var(--accent-red);
  }
  .brand-name { font-size: 30px; font-weight: 700; color: var(--brand-grey); letter-spacing: .2px; }
  .person-name { margin-top: 62px; font-size: 30px; color: var(--accent-red); }
  .person-title { margin-top: 2px; font-size: 19px; color: var(--ink); }
  .icon-divider {
    display: flex; align-items: center; justify-content: center; gap: 8px;
    margin: 14px 60px 12px;
  }
  .icon-divider .rule { flex: 1; height: 1px; background: var(--rule); }
  .contact-icon {
    width: 26px; height: 26px; background: var(--accent-red); border-radius: 3px;
    display: flex; align-items: center; justify-content: center;
  }
  .contact-list { font-size: 20px; line-height: 28px; }
  .rule-line { height: 1px; background: var(--rule); margin: 12px 70px; }
  .address { font-size: 20px; line-height: 28px; }
  .social-row {
    display: flex; align-items: center; justify-content: center; gap: 10px;
    margin: 16px 60px 0;
  }
  .social-row .rule { flex: 1; height: 1px; background: var(--rule); }
  .social-dot { width: 36px; height: 36px; border: 2px solid var(--ink); border-radius: 50%; }

  /* Back */
  .monogram-field {
    position: absolute; inset: 0 0 40% 0;
    background: linear-gradient(180deg, var(--pattern), var(--card));
  }
  .back-mark {
    position: absolute; top: 190px; right: 110px;
    width: 66px; height: 56px; border-radius: 50%; background: var(--accent-red);
  }
  .service-list {
    position: absolute; left: 0; right: 0; top: 330px;
    font-size: 20px; line-height: 28px;
  }
  .sep { color: var(--accent-red); padding: 0 4px; }
  .service-list .rule-line { margin: 10px 120px; }
</style>
</head>
<body>
<main class="stage">
  <section class="card card-front">
    <div class="brand-mark" aria-hidden="true"></div>
    <div class="brand-name">Talvex Engineering</div>
    <div class="person-name">Daniel Mwangi</div>
    <div class="person-title">Managing Director</div>
    <div class="icon-divider">
      <span class="rule"></span>
      <span class="contact-icon" aria-label="phone">
        <svg width="16" height="16" viewBox="0 0 24 24"><path fill="#1f2022" d="M6.6 10.8a15 15 0 0 0 6.6 6.6l2.2-2.2c.3-.3.7-.4 1-.2 1.1.4 2.3.6 3.6.6.6 0 1 .4 1 1V20c0 .6-.4 1-1 1A17 17 0 0 1 3 4c0-.6.4-1 1-1h3.5c.6 0 1 .4 1 1 0 1.3.2 2.5.6 3.6.1.3 0 .7-.2 1z"/></svg>
      </span>
      <span class="contact-icon" aria-label="email">
        <svg width="16" height="16" viewBox="0 0 24 24"><path fill="#1f2022" d="M2 5h20v14H2zm2 2v.5l8 5 8-5V7z"/></svg>
      </span>
      <span class="contact-icon" aria-label="address">
        <svg width="16" height="16" viewBox="0 0 24 24"><path fill="#1f2022" d="M12 2a7 7 0 0 0-7 7c0 5 7 13 7 13s7-8 7-13a7 7 0 0 0-7-7zm0 9.5A2.5 2.5 0 1 1 12 6.5a2.5 2.5 0 0 1 0 5z"/></svg>
      </span>
      <span class="rule"></span>
    </div>
    <div class="contact-list">
      <div>+ 254 20 555 0142/3</div>
      <div>info@talvex-eng.example</div>
      <div>www.talvex-eng.example</div>
    </div>
    <div class="rule-line"></div>
    <div class="address">
      <div>P.O. BOX 40512-80100</div>
      <div>Mombasa, Kenya</div>
    </div>
    <div class="social-row">
      <span class="rule"></span>
      <span class="social-dot" aria-label="social profile"></span>
      <span class="social-dot" aria-label="social profile"></span>
      <span class="rule"></span>
    </div>
  </section>

  <section class="card card-back">
    <div class="monogram-field" role="img" aria-label="Faint repeating company monogram pattern"></div>
    <div class="back-mark" aria-hidden="true"></div>
    <div class="service-list">
      <div>API 653 Tank Inspections</div>
      <div>API 570 Pipeline Inspections</div>
      <div>API 510 Pressure Vessel Inspections</div>
      <div>Welding Inspection<span class="sep">|</span>Electrical Inspection</div>
      <div>OCTG Inspections</div>
      <div>Lifting Equipment Inspections</div>
      <div class="rule-line"></div>
      <div>Non-Destructive Testing<span class="sep">|</span>Advanced NDT</div>
      <div>UT/PT/MT/RT/VT<span class="sep">|</span>PAUT/MFL/ILI</div>
      <div class="rule-line"></div>
      <div>Engineering Projects</div>
    </div>
  </section>
</main>
</body>
</html>
```